Velmora Builders LLC- Bus. Cards, Door Hangers, Invoice, Estimates, Postcards
I want a proffessional package that express who we are and what we do. www.velmora-builders.example
Velmora Builders LLC- Bus. Cards, Door Hangers, Invoice, Estimates, Postcards - Construction
Creative Brief
Professional
Calvin Tressel
Owner
4216 Pellham Ave. Denver, CO. 80417
calvin@velmora-builders.example
www.velmora-builders.example
Spray Foam Insulation Energy Auditing Weatherization Thermal Imaging

```html
<!DOCTYPE html>
<html lang="en">
<head>
<meta charset="utf-8">
<title>Velmora Builders – Business Card</title>
<link rel="stylesheet" href="https://fonts.googleapis.com/css2?family=Arimo:wght@400;700&display=swap">
<style>
  :root {
    --page: #ffffff;
    --ink: #111111;
    --frame: #3a3a3a;
    --divider: #141414;
    --brand-green: #3f9a2f;
    --panel-light: #9bd23a;
    --panel-mid: #4fb332;
    --panel-dark: #1f9a3a;
    --tagline: #2b2b2b;
  }
  * { margin: 0; padding: 0; box-sizing: border-box; }
  html, body {
    width: 1200px;
    height: 698px;
    overflow: hidden;
    background: var(--page);
  }
  .card {
    position: absolute;
    left: 29px;
    top: 24px;
    width: 1142px;
    height: 650px;
    border: 2px solid var(--frame);
    display: flex;
    font-family: "Arimo", Arial, sans-serif;
    color: var(--ink);
  }
  .card-front {
    position: relative;
    width: 557px;
    background: var(--page);
  }
  .brand {
    position: absolute;
    left: 80px;
    top: 300px;
    width: 440px;
  }
  .brand-name {
    display: flex;
    align-items: center;
    gap: 16px;
    color: var(--brand-green);
    font-size: 50px;
    font-weight: 400;
    line-height: 1;
    letter-spacing: -0.5px;
  }
  .brand-dot {
    width: 34px;
    height: 34px;
    border-radius: 50%;
    background: var(--brand-green);
    flex: none;
  }
  .brand-tagline {
    margin-top: 30px;
    font-size: 12.5px;
    letter-spacing: 1.6px;
    color: var(--tagline);
    white-space: nowrap;
  }
  .card-divider {
    width: 12px;
    background: var(--divider);
  }
  .card-back {
    position: relative;
    flex: 1;
    background: radial-gradient(ellipse 70% 60% at 45% 42%, var(--panel-light) 0%, var(--panel-mid) 45%, var(--panel-dark) 100%);
    color: var(--ink);
  }
  .holder {
    position: absolute;
    right: 22px;
    top: 58px;
    text-align: right;
  }
  .holder-name {
    font-size: 27px;
    font-weight: 700;
    line-height: 1.25;
  }
  .holder-role {
    font-size: 27px;
    font-weight: 400;
    line-height: 1.25;
  }
  .contact {
    position: absolute;
    left: 55px;
    top: 410px;
    font-size: 26px;
    line-height: 35px;
  }
  .contact-address { margin-bottom: 24px; }
  .contact-row { display: flex; white-space: nowrap; }
  .contact-label { width: 50px; }
  .contact-row + .contact-row { margin-top: 3px; }
</style>
</head>
<body>
  <div class="card">
    <section class="card-front">
      <div class="brand">
        <div class="brand-name"><span class="brand-dot"></span>Velmora Builders</div>
        <p class="brand-tagline">Crafting Comfort And Efficiency For Every Home</p>
      </div>
    </section>
    <div class="card-divider"></div>
    <section class="card-back">
      <div class="holder">
        <p class="holder-name">Calvin Tressel</p>
        <p class="holder-role">Owner</p>
      </div>
      <div class="contact">
        <p class="contact-address">4216 Pellham Ave.<br>Denver, CO. 80417</p>
        <p class="contact-row"><span class="contact-label">P :</span>631-555-0148</p>
        <p class="contact-row"><span class="contact-label">E :</span>calvin@velmora-builders.example</p>
        <p class="contact-row"><span class="contact-label">W :</span>www.velmora-builders.example</p>
      </div>
    </section>
  </div>
</body>
</html>
```